Simple Webpage for Company that offer IT Security Services

Company Type: Penetration Tests, IT Security Services, Security Audits
Company Name: NetBastion
Navigation Style: similar to https://www.veltrapro.com/en/ with Top Navigation (and submenu's)
Top Navigation Items: Services, About Us, Contact
Industry/Entity Type
It Company
Coding
Coded - Design and coding required

```html
<!DOCTYPE html>
<html lang="en">
<head>
<meta charset="utf-8">
<title>NetBastion – IT Security Services</title>
<link rel="stylesheet" href="https://fonts.googleapis.com/css2?family=Montserrat:wght@600;700;800&family=Open+Sans:wght@400;600;700&display=swap">
<style>
:root{
  --navy:#0a2f5c;
  --navy-deep:#062447;
  --ink:#111820;
  --text:#3a3f45;
  --muted:#6d737a;
  --grey-bg:#f4f4f4;
  --white:#ffffff;
  --gold:#f2c21b;
  --link:#5aa8ff;
  --rule:rgba(255,255,255,.22);
}
*{box-sizing:border-box;margin:0;padding:0}
html,body{width:1200px;height:2317px;overflow:hidden}
body{background:var(--white);font-family:"Open Sans",Arial,sans-serif;color:var(--text);position:relative}
h1,h2,h3,h4{font-family:"Montserrat",Arial,sans-serif}

/* Top navigation */
.site-header{height:65px;position:relative}
.main-nav{position:absolute;right:127px;top:23px;display:flex;gap:28px}
.main-nav a{font-family:"Montserrat",Arial,sans-serif;font-weight:700;font-size:13px;color:var(--navy);text-decoration:none;letter-spacing:-.2px}

/* Hero */
.hero{height:560px;position:relative;display:flex;flex-direction:column;align-items:center;
  background:linear-gradient(180deg,#2b3342 0%,#1c2636 45%,#232b37 75%,#151c27 100%)}
.hero-photo{position:absolute;inset:0;background:
  radial-gradient(ellipse at 30% 60%,rgba(140,120,100,.35),transparent 55%),
  radial-gradient(ellipse at 75% 45%,rgba(120,130,150,.3),transparent 50%),
  linear-gradient(180deg,rgba(10,20,40,.35),rgba(10,15,30,.55))}
.hero-title{position:relative;margin-top:254px;font-size:42px;font-weight:700;color:var(--white);letter-spacing:-.3px}
.hero-btn{position:relative;margin-top:14px;width:132px;height:33px;background:var(--navy);color:var(--white);
  font-family:"Montserrat",Arial,sans-serif;font-weight:700;font-size:13px;display:flex;align-items:center;justify-content:center;gap:8px;text-decoration:none}

/* About */
.about{height:353px;padding-top:62px}
.section-title{text-align:center;font-size:23px;font-weight:700;color:var(--ink);letter-spacing:-.6px}
.about-text{width:943px;margin:20px auto 0}
.about-text p{font-size:11.6px;line-height:22px;color:var(--text);margin-bottom:15px}

/* Services */
.services{margin-left:8px;height:628px;background:var(--grey-bg);padding-top:72px}
.service-grid{display:grid;grid-template-columns:repeat(3,307px);gap:22px 26px;margin:25px 0 0 105px}
.service-card{background:var(--white);height:193px;padding:40px 0 0 83px}
.service-card h3{font-size:15px;font-weight:600;color:var(--ink);letter-spacing:-.3px}
.service-card p{width:188px;font-size:11.5px;line-height:15.5px;color:var(--muted);margin-top:11px}
.read-more{display:flex;align-items:center;gap:8px;margin-top:14px;font-family:"Montserrat",Arial,sans-serif;font-weight:700;font-size:11px;color:var(--ink);text-decoration:none}

/* Stats band */
.stats{margin:0 8px;height:321px;position:relative;overflow:hidden;
  background:linear-gradient(100deg,#0c1c36 0%,#10294c 45%,#163a66 70%,#0d2240 100%)}
.stats-photo{position:absolute;inset:0;background:
  radial-gradient(circle at 12% 30%,rgba(120,150,190,.35),transparent 18%),
  radial-gradient(circle at 35% 80%,rgba(110,140,180,.25),transparent 15%),
  radial-gradient(ellipse at 78% 70%,rgba(60,90,140,.6),transparent 40%)}
.stats-title{position:relative;padding:66px 0 0 92px;font-size:34px;font-weight:800;color:var(--white);line-height:40px;letter-spacing:-1.6px;width:760px}
.stats-list{position:relative;display:flex;margin:24px 0 0 92px}
.stat{width:168px}
.stat p{font-family:"Montserrat",Arial,sans-serif;font-weight:700;font-size:11.5px;line-height:15px;color:var(--white);margin-top:14px;letter-spacing:-.4px}

/* Footer */
.site-footer{height:390px;background:var(--navy);padding:88px 113px 0}
.footer-cols{display:grid;grid-template-columns:repeat(4,224px);gap:26px}
.footer-col h4{font-size:21px;font-weight:700;color:var(--white);letter-spacing:-.8px;padding-bottom:14px;border-bottom:1px solid var(--rule)}
.footer-col p{font-size:11px;line-height:19px;color:var(--white);margin-top:32px}
.footer-col ul{margin-top:34px;padding-left:18px}
.footer-col li{font-size:11px;line-height:23px;color:var(--white)}
.contact-list{list-style:none;margin-top:32px}
.contact-list li{display:flex;gap:8px;font-size:11px;line-height:23px;color:var(--white)}
.contact-list svg{flex:none;margin-top:6px}
.contact-list a{color:var(--link);text-decoration:none}
.footer-bottom{margin-top:52px;border-top:1px solid var(--rule);padding-top:20px;font-size:11px;color:#a9bdd6}
</style>
</head>
<body>

<header class="site-header">
  <nav class="main-nav">
    <a href="#">Home</a><a href="#">About Us</a><a href="#">Our Services</a><a href="#">Contact Us</a>
  </nav>
</header>

<section class="hero">
  <div class="hero-photo" role="img" aria-label="Photo of a busy open-plan security operations office"></div>
  <h1 class="hero-title">Duis Autem Velenum Dolor</h1>
  <a class="hero-btn" href="#">Read More
    <svg width="8" height="11" viewBox="0 0 8 11"><path d="M2 1l4.5 4.5L2 10" fill="none" stroke="#fff" stroke-width="2"/></svg>
  </a>
</section>

<section class="about">
  <h2 class="section-title">About NetBastion</h2>
  <div class="about-text">
    <p>Lorem ipsum dolor sit amet consetetur sadipscing elitr sed diam nonumy eirmod tempor invidunt ut labore et dolore magna aliquyam erat sed diam voluptua. At vero eos et accusam et justo duo dolores et ea rebum. Stet clita kasd gubergren, no sea takimata sanctus est Lorem ipsum dolor sit amet. Lorem ipsum dolor sit amet, consetetur sadipscing elitr sed diam nonumy eirmod tempor invidunt ut labore et dolore magna aliquyam erat sed diam voluptua. Lorem ipsum dolor sit amet consetetur sadipscing elitr sed diam nonumy eirmod tempor invidunt ut labore et dolore magna aliquyam erat sed diam voluptua.</p>
    <p>At vero eos et accusam et justo duo dolores et ea rebum. Stet clita kasd gubergren, no sea takimata sanctus est Lorem ipsum dolor sit amet. Lorem ipsum dolor sit amet consetetur sadipscing elitr sed diam nonumy eirmod tempor invidunt ut labore et dolore magna aliquyam erat sed diam voluptua. At vero eos et accusam et justo duo dolores et ea rebum. Stet clita kasd gubergren, no sea takimata sanctus est Lorem ipsum dolor sit amet.</p>
  </div>
</section>

<section class="services">
  <h2 class="section-title">Our Services</h2>
  <div class="service-grid">
    <article class="service-card"><h3>Penetration Tests</h3><p>Lorem ipsum dolor sit amet consetetur sadipscing elitr sed diam nonumy eirmod tempor invidunt sed dolore aliquyam.</p><a class="read-more" href="#">Read more <svg width="6" height="9" viewBox="0 0 6 9"><path d="M1 1l3.5 3.5L1 8" fill="none" stroke="var(--gold)" stroke-width="1.8"/></svg></a></article>
    <article class="service-card"><h3>IT Security Services</h3><p>Lorem ipsum dolor sit amet consetetur sadipscing elitr sed diam nonumy eirmod tempor invidunt sed dolore aliquyam.</p><a class="read-more" href="#">Read more <svg width="6" height="9" viewBox="0 0 6 9"><path d="M1 1l3.5 3.5L1 8" fill="none" stroke="var(--gold)" stroke-width="1.8"/></svg></a></article>
    <article class="service-card"><h3>Security Audits</h3><p>Lorem ipsum dolor sit amet consetetur sadipscing elitr sed diam nonumy eirmod tempor invidunt sed dolore aliquyam.</p><a class="read-more" href="#">Read more <svg width="6" height="9" viewBox="0 0 6 9"><path d="M1 1l3.5 3.5L1 8" fill="none" stroke="var(--gold)" stroke-width="1.8"/></svg></a></article>
    <article class="service-card"><h3>Security Consultancy</h3><p>Lorem ipsum dolor sit amet consetetur sadipscing elitr sed diam nonumy eirmod tempor invidunt sed dolore aliquyam.</p><a class="read-more" href="#">Read more <svg width="6" height="9" viewBox="0 0 6 9"><path d="M1 1l3.5 3.5L1 8" fill="none" stroke="var(--gold)" stroke-width="1.8"/></svg></a></article>
    <article class="service-card"><h3>Security Training</h3><p>Lorem ipsum dolor sit amet consetetur sadipscing elitr sed diam nonumy eirmod tempor invidunt sed dolore aliquyam.</p><a class="read-more" href="#">Read more <svg width="6" height="9" viewBox="0 0 6 9"><path d="M1 1l3.5 3.5L1 8" fill="none" stroke="var(--gold)" stroke-width="1.8"/></svg></a></article>
    <article class="service-card"><h3>Forensic Experts</h3><p>Lorem ipsum dolor sit amet consetetur sadipscing elitr sed diam nonumy eirmod tempor invidunt sed dolore aliquyam.</p><a class="read-more" href="#">Read more <svg width="6" height="9" viewBox="0 0 6 9"><path d="M1 1l3.5 3.5L1 8" fill="none" stroke="var(--gold)" stroke-width="1.8"/></svg></a></article>
  </div>
</section>

<section class="stats">
  <div class="stats-photo" role="img" aria-label="Photo of a businessman in a suit holding a tablet over a blurred bokeh background"></div>
  <h2 class="stats-title">Duis autem veleum iriure dolor in hendrerit vulputate velit esse molestie consequat</h2>
  <div class="stats-list">
    <div class="stat"><svg width="36" height="42" viewBox="0 0 36 42"><path d="M18 2L3 7v12c0 10 6.5 17.5 15 21 8.5-3.5 15-11 15-21V7z" fill="none" stroke="var(--gold)" stroke-width="3"/><path d="M10.5 21l5.5 5.5 10-11" fill="none" stroke="var(--gold)" stroke-width="3.5"/></svg><p>1500+ Penetration<br>Test Projects</p></div>
    <div class="stat"><svg width="36" height="42" viewBox="0 0 36 42"><path d="M18 2L3 7v12c0 10 6.5 17.5 15 21 8.5-3.5 15-11 15-21V7z" fill="none" stroke="var(--gold)" stroke-width="3"/><path d="M10.5 21l5.5 5.5 10-11" fill="none" stroke="var(--gold)" stroke-width="3.5"/></svg><p>1000+ IT Security<br>Services</p></div>
    <div class="stat"><svg width="36" height="42" viewBox="0 0 36 42"><path d="M18 2L3 7v12c0 10 6.5 17.5 15 21 8.5-3.5 15-11 15-21V7z" fill="none" stroke="var(--gold)" stroke-width="3"/><path d="M10.5 21l5.5 5.5 10-11" fill="none" stroke="var(--gold)" stroke-width="3.5"/></svg><p>1000+ Security<br>Audits</p></div>
    <div class="stat"><svg width="36" height="42" viewBox="0 0 36 42"><path d="M18 2L3 7v12c0 10 6.5 17.5 15 21 8.5-3.5 15-11 15-21V7z" fill="none" stroke="var(--gold)" stroke-width="3"/><path d="M10.5 21l5.5 5.5 10-11" fill="none" stroke="var(--gold)" stroke-width="3.5"/></svg><p>500+ IT Security<br>Training</p></div>
  </div>
</section>

<footer class="site-footer">
  <div class="footer-cols">
    <div class="footer-col">
      <h4>About NetBastion</h4>
      <p>Lorem ipsum dolor sit amet consetetur sadipscing elitr sed diam nonumy eirmod tempor invidunt ut labore et dolore magna aliquyam erat sed diam voluptua. At vero eos et accusam et justo duo dolores et ea rebum. Stet clita kasd gubergren nosea takimata sanctus est.</p>
    </div>
    <div class="footer-col">
      <h4>Our Services</h4>
      <ul><li>Penetration Tests</li><li>IT Security Services</li><li>Security Audits</li><li>Security Consultancy</li><li>Security Training</li><li>Forensic Experts</li></ul>
    </div>
    <div class="footer-col">
      <h4>Useful Links</h4>
      <ul><li>Home</li><li>About Us</li><li>Our Services</li><li>Contact Us</li></ul>
    </div>
    <div class="footer-col">
      <h4>Contact Us</h4>
      <ul class="contact-list">
        <li><svg width="9" height="12" viewBox="0 0 9 12"><path d="M4.5 11S1 6.8 1 4.5a3.5 3.5 0 017 0C8 6.8 4.5 11 4.5 11z" fill="none" stroke="#fff" stroke-width="1.3"/><circle cx="4.5" cy="4.5" r="1.2" fill="#fff"/></svg><span>Stet clita kasd gubergren nosea<br>takimata sanctus eoset accusam</span></li>
        <li><svg width="11" height="11" viewBox="0 0 11 11"><path d="M2 1l2 2.2-1 1.3a6 6 0 003.5 3.5l1.3-1L10 9l-1.3 1.5C5 10.5.5 6 .5 2.3z" fill="none" stroke="#fff" stroke-width="1.2"/></svg><span>+123-4567-890</span></li>
        <li><svg width="11" height="11" viewBox="0 0 11 11"><path d="M2 1l2 2.2-1 1.3a6 6 0 003.5 3.5l1.3-1L10 9l-1.3 1.5C5 10.5.5 6 .5 2.3z" fill="none" stroke="#fff" stroke-width="1.2"/></svg><span>+123-4567-890</span></li>
        <li><svg width="11" height="10" viewBox="0 0 11 10"><rect x=".6" y="1.2" width="9.8" height="7.6" fill="none" stroke="#fff" stroke-width="1.2"/><path d="M.6 1.4l4.9 4 4.9-4" fill="none" stroke="#fff" stroke-width="1.2"/></svg><a href="#">support@netbastion.com</a></li>
      </ul>
    </div>
  </div>
  <div class="footer-bottom">Copyright © 2017 NetBastion. All Rights Reserved.</div>
</footer>

</body>
</html>
```